Simple : A Therapist is looking for a Design

Im lookind for a business card design for my new business .
my therapy field - Stillpoint Cranial .
Its part of Osteopatic medicine .
its gental, not invasive method that focus on the bones of the skull (cranial) .
i want some kind of skull in it like the attached photo.

Target Market(s)

people that suffer from pain

Industry/Entity Type

Physical Therapy

Contact Information for Business Card

i want people to understand this is diffrent kind of therapy
its anatomy base , gental and give outstanding result .

Font styles to use
Serif

Colors
fee18a
cadf82
fbc994
cedeed
fbe7d2
fff3d1

Requirements
Must have
• one side: my name (Yoram Shefet) ,
• phone number ( 0521746098)
• email (shefetyoram@postvela.com)
• other side : Stillpoint Cranial
Nice to have
• i want some kind of skull in it like the attached photo.
• very powrful, accurate and smart.
• nice colores (maybe lite orange?, lite green?) , simple, relax, smart

```html
<!DOCTYPE html>
<html lang="en">
<head>
<meta charset="utf-8">
<title>Stillpoint Cranial – Business Card</title>
<link href="https://fonts.googleapis.com/css2?family=Cinzel:wght@400;500&family=Lato:wght@400&display=swap" rel="stylesheet">
<style>
  :root {
    --green: #cadf82;
    --green-deep: #b5cf5e;
    --peach: #fbc994;
    --orange: #f5b57f;
    --text-grey: #8a8a8a;
    --contact-grey: #6f6f6f;
    --paper: #ffffff;
    --backdrop: #ecebe8;
  }
  * { margin: 0; padding: 0; box-sizing: border-box; }
  html, body {
    width: 1200px; height: 900px; overflow: hidden;
    background: var(--backdrop);
  }
  .canvas { position: relative; width: 1200px; height: 900px; }

  .card {
    position: absolute; width: 700px; height: 400px;
    overflow: hidden;
    box-shadow: 0 6px 18px rgba(0,0,0,0.12);
  }

  /* Back side */
  .card-back {
    left: 110px; top: 50px;
    background: linear-gradient(180deg, var(--green) 0%, var(--peach) 100%);
    display: flex; align-items: center; justify-content: center;
  }
  .brand { display: flex; align-items: center; gap: 16px; }
  .brand-dot { width: 26px; height: 26px; border-radius: 50%; flex: none; }
  .brand-name {
    font-family: "Cinzel", serif; font-weight: 400;
    font-size: 30px; letter-spacing: 4px; line-height: 1; white-space: nowrap;
  }
  .card-back .brand-dot { background: var(--paper); }
  .card-back .brand-name { color: var(--paper); }

  /* Front side */
  .card-front {
    left: 390px; top: 440px;
    background: var(--paper);
  }
  .footer-band {
    position: absolute; left: 0; right: 0; bottom: 0; height: 70px;
    background: var(--green);
  }
  .footer-rule {
    position: absolute; left: 0; right: 0; bottom: 78px; height: 6px;
    background: var(--peach);
  }
  .holder-name {
    position: absolute; left: 52px; top: 62px;
    font-family: "Cinzel", serif; font-weight: 500;
    font-size: 28px; letter-spacing: 1px; line-height: 1.2; white-space: nowrap;
  }
  .holder-name .first { color: var(--orange); }
  .holder-name .last { color: var(--green-deep); }
  .card-front .brand {
    position: absolute; right: 40px; top: 130px;
  }
  .card-front .brand-dot { background: var(--green); width: 22px; height: 22px; }
  .card-front .brand-name { color: var(--text-grey); font-size: 24px; letter-spacing: 3px; }

  .contact {
    position: absolute; left: 52px; top: 220px;
    list-style: none;
    font-family: "Lato", sans-serif; font-size: 19px; color: var(--contact-grey);
  }
  .contact li { display: flex; align-items: center; gap: 10px; line-height: 30px; }
  .contact svg { width: 18px; height: 18px; fill: var(--orange); flex: none; }
</style>
</head>
<body>
<main class="canvas">

  <section class="card card-back" aria-label="Card back">
    <div class="brand">
      <span class="brand-dot"></span>
      <span class="brand-name">Stillpoint Cranial</span>
    </div>
  </section>

  <section class="card card-front" aria-label="Card front">
    <div class="footer-rule"></div>
    <div class="footer-band"></div>

    <h1 class="holder-name"><span class="first">YORAM</span> <span class="last">SHEFET</span></h1>

    <div class="brand">
      <span class="brand-dot"></span>
      <span class="brand-name">Stillpoint Cranial</span>
    </div>

    <ul class="contact">
      <li>
        <svg viewBox="0 0 24 24" aria-hidden="true"><path d="M6.6 10.8a15.1 15.1 0 0 0 6.6 6.6l2.2-2.2c.3-.3.7-.4 1-.2 1.1.4 2.3.6 3.6.6.6 0 1 .4 1 1V20c0 .6-.4 1-1 1A17 17 0 0 1 3 4c0-.6.4-1 1-1h3.5c.6 0 1 .4 1 1 0 1.3.2 2.5.6 3.6.1.3 0 .7-.2 1z"/></svg>
        <span>0521746098</span>
      </li>
      <li>
        <svg viewBox="0 0 24 24" aria-hidden="true"><path d="M2 5h20v14H2z M4 7v.4l8 5.2 8-5.2V7z" fill-rule="evenodd"/></svg>
        <span>shefetyoram@postvela.com</span>
      </li>
    </ul>
  </section>

</main>
</body>
</html>
```